Business card for Property Management consultant

I need a business card for my business LX Vantage - I consult to real estate agents to improve the performance of their Property Management departments (rental houses management). The card needs to be very professional looking, incorporating our logo and my photo plus the line "Develop your Rent Roll to Perform"

Target Market(s)

Real Estate business owners

Industry/Entity Type

Business Consultant

Contact Information for Business Card

Business name - LX Vantage (logo uploaded)
My Name : Marcia Kellaway -
Title : Property Management Consultant

Develop your Rent Roll to perform

Phone : +61 438592716
email : marcia@lxvantage.com.au
website ; www.lxvantage.com.au

Requirements
Must have
• Logo
• My photo
• Very corporate / professional look

```html
<!DOCTYPE html>
<html lang="en">
<head>
<meta charset="utf-8">
<title>LX Vantage – Business Card</title>
<link rel="stylesheet" href="https://fonts.googleapis.com/css2?family=Jost:wght@400;500&display=swap">
<style>
  :root {
    --backdrop: #4b4b4b;
    --card: #ffffff;
    --ink: #231f20;
    --gold: #c8922a;
    --blue: #2f5fb3;
    --photo-top: #e9d6cc;
    --photo-mid: #8a4a34;
    --photo-low: #2e5fb8;
  }
  * { margin: 0; padding: 0; box-sizing: border-box; }
  html, body { width: 1200px; height: 1200px; overflow: hidden; }
  body { background: var(--backdrop); position: relative; font-family: "Jost", sans-serif; font-weight: 400; color: var(--ink); }

  .card {
    position: absolute; left: 276px; width: 646px; height: 366px;
    background: var(--card); overflow: hidden;
    box-shadow: 0 6px 14px rgba(0,0,0,0.35);
  }
  .card--front { top: 206px; }
  .card--back  { top: 628px; }

  .brand { position: absolute; display: flex; align-items: center; font-family: "Jost", sans-serif; font-weight: 500; color: var(--ink); white-space: nowrap; line-height: 1; }
  .brand__mark { background: var(--gold); flex: none; }

  .card--front .brand { left: 24px; top: 62px; font-size: 44px; gap: 12px; }
  .card--front .brand__mark { width: 36px; height: 36px; }

  .person__accent { position: absolute; left: 0; top: 182px; width: 12px; height: 42px; background: var(--gold); }
  .person__name { position: absolute; left: 32px; top: 178px; font-size: 21px; font-weight: 400; color: var(--gold); line-height: 1.2; }
  .person__title { position: absolute; left: 32px; top: 208px; font-size: 15px; color: var(--ink); line-height: 1.2; }

  .contact { position: absolute; left: 32px; top: 246px; list-style: none; font-size: 15px; }
  .contact li { display: flex; align-items: center; height: 22px; gap: 8px; }
  .contact svg { width: 15px; height: 15px; flex: none; }

  .slogan { position: absolute; left: 32px; top: 328px; font-size: 15.5px; color: var(--blue); line-height: 1.2; }

  .portrait {
    position: absolute; right: 0; top: 0; width: 326px; height: 366px;
    background: linear-gradient(180deg, #ffffff 0%, var(--photo-top) 25%, var(--photo-mid) 45%, var(--photo-low) 78%, var(--photo-low) 100%);
    clip-path: polygon(28% 100%, 35% 70%, 25% 20%, 50% 4%, 90% 10%, 100% 40%, 100% 100%);
  }

  .card--back .brand { left: 0; right: 0; top: 138px; justify-content: center; font-size: 76px; gap: 20px; }
  .card--back .brand__mark { width: 60px; height: 60px; }
</style>
</head>
<body>
  <section class="card card--front">
    <div class="brand"><span class="brand__mark"></span><span class="brand__name">LX Vantage</span></div>

    <span class="person__accent"></span>
    <h1 class="person__name">Marcia Kellaway</h1>
    <p class="person__title">Property Management Consultant</p>

    <ul class="contact">
      <li>
        <svg viewBox="0 0 16 16" fill="var(--blue)"><path d="M2 6c0-2 2.5-3 6-3s6 1 6 3v1h-3V5.5C10 5 9 4.8 8 4.8S6 5 5 5.5V7H2z"/><path d="M4 8h8l1 5H3z"/><circle cx="8" cy="10.5" r="1.3" fill="#fff"/></svg>
        <span>+61 438592716</span>
      </li>
      <li>
        <svg viewBox="0 0 16 16"><rect x="1.5" y="3.5" width="13" height="9" fill="var(--blue)"/><path d="M1.5 3.5 8 9l6.5-5.5" fill="none" stroke="#fff" stroke-width="1"/></svg>
        <span>marcia@lxvantage.com.au</span>
      </li>
      <li>
        <svg viewBox="0 0 16 16" fill="none" stroke="var(--blue)" stroke-width="1.1"><circle cx="8" cy="8" r="6.5"/><ellipse cx="8" cy="8" rx="3" ry="6.5"/><path d="M1.5 8h13M2.5 4.8h11M2.5 11.2h11"/></svg>
        <span>www.lxvantage.com.au</span>
      </li>
    </ul>

    <p class="slogan">Develop your Rent Roll to perform</p>

    <div class="portrait" role="img" aria-label="Portrait photo of Marcia Kellaway in a blue blazer"></div>
  </section>

  <section class="card card--back">
    <div class="brand"><span class="brand__mark"></span><span class="brand__name">LX Vantage</span></div>
  </section>
</body>
</html>
```